Book Cover for a technology book - The Silent Lattice

We are writing a book that is a handbook how to build a hybrid cloud - this is a technology concept where companies use cloud services both from the like of Vornix or Plenquor and also cloud services built in there own data centers - hence the term hybrid cloud. We want a book cover with the title - The Silent Lattice; which signifies that we will be teaching companies how to build a hybrid cloud that just works. We want the tagline - handbook for building Hybrid Clouds. The authors are Corwin Haddle and Ross Pelley. The cover is to be engaging and feel different than your usual technical manual. I don't have any graphics to help out however will be able to refine and tell you what I don and don't like based on your drafts. The book dimensions are yet to be determined, in the first instance it will be a PDF

Target Market(s)

technology executives and specialists

Industry/Entity Type

Information Technology

Colors

Designer to choose colors to be used in the design.

Requirements
Nice to have
• While I don't have a particular view to how it will look, I'd like the style to be more casual than ultra formal

```html
<!DOCTYPE html>
<html lang="en">
<head>
<meta charset="utf-8">
<title>The Silent Lattice — Book Cover</title>
<link rel="stylesheet" href="https://fonts.googleapis.com/css2?family=Barlow:wght@500;600&family=Barlow+Semi+Condensed:wght@500;600&display=swap">
<style>
  :root {
    --navy: #023a56;
    --cyan: #1fc3ea;
    --band: #00ccf2;
    --white: #ffffff;
    --ink: #0b3a55;
    --glow-core: #29b8e3;
    --glow-edge: #0f6f97;
  }
  html, body {
    margin: 0;
    padding: 0;
    width: 800px;
    height: 1200px;
    overflow: hidden;
    background: var(--navy);
  }
  .cover {
    position: relative;
    width: 800px;
    height: 1200px;
    background: var(--navy);
    overflow: hidden;
  }
  .title {
    position: absolute;
    left: 0;
    top: 0;
    margin: 0;
    font-family: "Barlow", sans-serif;
    font-weight: 600;
    color: var(--white);
    font-size: 190px;
    line-height: 1;
    letter-spacing: -2px;
  }
  .title-line {
    position: absolute;
    white-space: nowrap;
  }
  .title-line--first { left: 60px; top: 202px; }
  .title-line--second { left: 66px; top: 374px; }
  .title-line--third { left: 66px; top: 546px; }
  .idea-artwork {
    position: absolute;
    left: 390px;
    top: 194px;
    width: 154px;
    height: 236px;
    border-radius: 6px;
    background: radial-gradient(ellipse at 50% 42%, var(--glow-core) 0%, var(--glow-edge) 100%);
  }
  .tagline {
    position: absolute;
    left: 0;
    right: 0;
    top: 756px;
    margin: 0;
    text-align: center;
    font-family: "Barlow Semi Condensed", sans-serif;
    font-weight: 500;
    font-size: 47px;
    line-height: 1;
    letter-spacing: -0.5px;
  }
  .tagline-lead { color: var(--cyan); }
  .tagline-subject { color: var(--white); }
  .author-band {
    position: absolute;
    left: 0;
    top: 1020px;
    width: 800px;
    height: 180px;
    background: var(--band);
    display: flex;
    align-items: center;
    justify-content: center;
    box-sizing: border-box;
    padding-bottom: 12px;
  }
  .authors {
    margin: 0;
    font-family: "Barlow Semi Condensed", sans-serif;
    font-weight: 600;
    font-size: 43px;
    color: var(--ink);
    letter-spacing: -0.3px;
  }
</style>
</head>
<body>
  <main class="cover">
    <h1 class="title">
      <span class="title-line title-line--first">The</span>
      <span class="title-line title-line--second">Silent</span>
      <span class="title-line title-line--third">Lattice</span>
    </h1>

    <div class="idea-artwork" role="img" aria-label="Illustration of a light bulb built from a network of connected cloud service icons"></div>

    <p class="tagline">
      <span class="tagline-lead">Handbook for building</span>
      <span class="tagline-subject">Hybrid Clouds</span>
    </p>

    <footer class="author-band">
      <p class="authors">Corwin Haddle and Ross Pelley</p>
    </footer>
  </main>
</body>
</html>
```